Dental Business Card

I need Dental oriented business cards.
On the front side -
- on the first line, my name:
Dr Marlo Vintner
- on the second line (just underneath):
Doctor of Dental Medicine
- on the third line, or underneath that or in a corner, I would like the address and phone number:
5182 Ch. Birchfield
Montreal QC H2T 4B9
514-629-5074
- other than that i would maybe like a logo of a tooth, but i want it to be subtle and very basic!
- I would like the card to be preferably black or dark grey-ish with the writing in white
On the other side -
- 2-3 lines with the possibility to write the next appointment the box with the lines should be white, with the rest of the card being black

```html
<!DOCTYPE html>
<html lang="en">
<head>
<meta charset="utf-8">
<title>Dental Business Card</title>
<link rel="stylesheet" href="https://fonts.googleapis.com/css2?family=Lato:wght@400;700&family=Libre+Baskerville:wght@400&display=swap">
<style>
  :root {
    --page-bg: #141414;
    --card-bg: #262626;
    --ink: #ffffff;
    --ink-soft: #e6e6e6;
    --rule: #bdbdbd;
  }
  * { box-sizing: border-box; margin: 0; padding: 0; }
  html, body { width: 1200px; height: 895px; overflow: hidden; }
  body {
    background: var(--page-bg);
    display: flex;
    flex-direction: column;
    align-items: center;
    justify-content: center;
    gap: 30px;
    font-family: "Lato", Arial, sans-serif;
    color: var(--ink);
  }
  .card {
    position: relative;
    width: 700px;
    height: 400px;
    background: var(--card-bg);
    box-shadow: 0 10px 30px rgba(0,0,0,0.6);
  }
  /* Back side */
  .appointment-label {
    position: absolute;
    left: 120px;
    top: 128px;
    font-weight: 700;
    font-size: 20px;
    letter-spacing: 0.3px;
  }
  .appointment-lines {
    position: absolute;
    left: 120px;
    top: 162px;
    display: flex;
    flex-direction: column;
    gap: 14px;
  }
  .appointment-line {
    width: 470px;
    height: 34px;
    background: var(--ink);
  }
  /* Front side */
  .brand {
    position: absolute;
    left: 60px;
    top: 180px;
    width: 210px;
    display: flex;
    align-items: center;
    gap: 12px;
    font-family: "Lato", Arial, sans-serif;
    font-size: 20px;
    font-weight: 400;
    color: var(--ink);
  }
  .brand-dot {
    width: 14px;
    height: 14px;
    border-radius: 50%;
    border: 2px solid var(--ink);
    flex: none;
  }
  .divider {
    position: absolute;
    left: 295px;
    top: 110px;
    width: 1px;
    height: 190px;
    background: var(--rule);
  }
  .contact {
    position: absolute;
    left: 325px;
    top: 108px;
  }
  .contact-name {
    font-family: "Libre Baskerville", Georgia, serif;
    font-size: 30px;
    font-weight: 400;
    text-transform: uppercase;
    letter-spacing: 0.5px;
    line-height: 1.1;
  }
  .contact-title {
    font-size: 21px;
    color: var(--ink-soft);
    margin-bottom: 18px;
  }
  .contact-address {
    font-size: 21px;
    line-height: 1.35;
    color: var(--ink-soft);
    font-style: normal;
    margin-bottom: 12px;
  }
  .contact-phone {
    display: flex;
    align-items: center;
    gap: 10px;
    font-size: 21px;
    color: var(--ink-soft);
  }
  .contact-phone svg { width: 16px; height: 16px; }
</style>
</head>
<body>
  <section class="card card-back" aria-label="Card back">
    <p class="appointment-label">Next Appointment</p>
    <div class="appointment-lines">
      <div class="appointment-line"></div>
      <div class="appointment-line"></div>
      <div class="appointment-line"></div>
    </div>
  </section>

  <section class="card card-front" aria-label="Card front">
    <div class="brand"><span class="brand-dot"></span><span>Vintner Dental</span></div>
    <div class="divider"></div>
    <div class="contact">
      <h1 class="contact-name">Dr Marlo Vintner</h1>
      <p class="contact-title">Doctor of Dental Medicine</p>
      <address class="contact-address">5182 Ch. Birchfield<br>Montreal QC H2T 4B9</address>
      <p class="contact-phone">
        <svg viewBox="0 0 24 24" aria-hidden="true"><path fill="#ffffff" d="M6.6 10.8a15.5 15.5 0 0 0 6.6 6.6l2.2-2.2c.3-.3.7-.4 1-.2 1.1.4 2.3.6 3.6.6.6 0 1 .4 1 1V20c0 .6-.4 1-1 1C10.6 21 3 13.4 3 4c0-.6.4-1 1-1h3.5c.6 0 1 .4 1 1 0 1.3.2 2.5.6 3.6.1.3 0 .7-.2 1z"/></svg>
        <span>514-629-5074</span>
      </p>
    </div>
  </section>
</body>
</html>
```